Harborline Crest Insurance Services

we are a high end insurance agency we specialize on Auto | Home | Business | Life looking for something professional and luxuries at the same time. if you guys need anything else please let me know.

Auto | Home | Business | Life must be under logo on the back with black background.

i want the back part to be black with our gold logo on it.

Target Market(s)

Auto | Home | Business | Life

Industry/Entity Type

Insurance Broker

Contact Information for Business Card

My logo is gold so a black in the back would be nice.

Font styles to use
Serif

Colors
000000

Requirements
Must have
• Big logo on the back with black background.

```html
<!DOCTYPE html>
<html lang="en">
<head>
<meta charset="utf-8">
<title>Harborline Crest Insurance Services – Business Card</title>
<link rel="stylesheet" href="https://fonts.googleapis.com/css2?family=Cinzel:wght@600&family=Tinos:wght@400;700&display=swap">
<style>
  :root {
    --stage: #3b3431;
    --black: #050505;
    --panel: #2d2d2e;
    --gold: #f2bd25;
    --silver: #b9b9bd;
    --text-light: #d9d9d9;
    --text-dark: #1a1a1a;
  }
  * { box-sizing: border-box; margin: 0; padding: 0; }
  html, body { width: 1200px; height: 780px; overflow: hidden; }
  body {
    background: var(--stage);
    font-family: "Tinos", "Times New Roman", serif;
    position: relative;
  }
  .card {
    position: absolute;
    width: 540px;
    height: 310px;
    background: var(--black);
    overflow: hidden;
    box-shadow: 0 14px 30px rgba(0,0,0,.45);
  }
  .card--back { left: 50px; top: 60px; }
  .card--front { left: 610px; top: 410px; }

  /* wordmark */
  .wordmark {
    position: absolute;
    display: flex;
    align-items: center;
    gap: 16px;
  }
  .wordmark__dot {
    width: 58px; height: 58px;
    border-radius: 50%;
    background: var(--gold);
    flex: none;
  }
  .wordmark__name {
    font-family: "Cinzel", "Times New Roman", serif;
    font-weight: 600;
    color: var(--gold);
    line-height: 1.05;
  }
  .wordmark__name span { display: block; }
  .wordmark__name .line-1 { font-size: 34px; }
  .wordmark__name .line-2 { font-size: 15.5px; letter-spacing: 4.4px; margin-top: 4px; }
  .card--back .wordmark { left: 84px; top: 64px; }
  .card--front .wordmark { left: 110px; top: 34px; transform: scale(.9); transform-origin: left top; }

  /* back card */
  .back__services {
    position: absolute; left: 158px; top: 150px;
    font-size: 15px; letter-spacing: 2px;
    color: var(--text-light);
  }
  .back__rule {
    position: absolute; left: 0; right: 0; top: 228px;
    height: 6px; background: var(--silver);
  }
  .back__band {
    position: absolute; left: 0; right: 0; top: 234px; bottom: 0;
    background: var(--gold);
    display: flex; align-items: center; justify-content: center;
  }
  .back__web { font-size: 15px; color: var(--text-dark); }

  /* front card */
  .front__rule {
    position: absolute; left: 0; right: 0; top: 132px;
    height: 6px; background: var(--gold);
  }
  .front__panel {
    position: absolute; left: 0; right: 0; top: 138px; height: 120px;
    background: var(--panel);
  }
  .front__person {
    position: absolute; left: 40px; top: 160px; width: 190px;
    text-align: right;
  }
  .person__name { font-size: 22px; font-weight: 700; color: var(--gold); }
  .person__role { font-size: 16px; color: var(--text-light); margin-top: 2px; }
  .front__divider {
    position: absolute; left: 250px; top: 160px;
    width: 1px; height: 76px; background: #8a8a8a;
  }
  .front__contacts {
    position: absolute; left: 268px; top: 160px;
    list-style: none;
  }
  .contact {
    display: flex; align-items: center; gap: 8px;
    font-size: 15px; color: var(--text-light);
    height: 25px;
  }
  .contact svg { width: 15px; height: 15px; flex: none; fill: var(--gold); }
  .front__band {
    position: absolute; left: 0; right: 0; top: 258px; bottom: 0;
    background: var(--gold);
    display: flex; align-items: center; justify-content: center;
  }
  .front__address { font-size: 16px; color: var(--text-dark); }
</style>
</head>
<body>

<section class="card card--back" aria-label="Card back">
  <div class="wordmark">
    <div class="wordmark__dot"></div>
    <div class="wordmark__name"><span class="line-1">Harborline Crest</span><span class="line-2">Insurance Services</span></div>
  </div>
  <p class="back__services">Auto | Home | Business | Life</p>
  <div class="back__rule"></div>
  <div class="back__band"><p class="back__web">www.harborlinecrest.com</p></div>
</section>

<section class="card card--front" aria-label="Card front">
  <div class="wordmark">
    <div class="wordmark__dot"></div>
    <div class="wordmark__name"><span class="line-1">Harborline Crest</span><span class="line-2">Insurance Services</span></div>
  </div>
  <div class="front__rule"></div>
  <div class="front__panel"></div>

  <div class="front__person">
    <p class="person__name">Evan Marlow</p>
    <p class="person__role">Managing Director</p>
  </div>
  <div class="front__divider"></div>
  <ul class="front__contacts">
    <li class="contact">
      <svg viewBox="0 0 16 16" aria-hidden="true"><path d="M3 1h3l1.5 4-2 1.3a9 9 0 0 0 4.2 4.2L11 8.5l4 1.5v3a2 2 0 0 1-2 2A12 12 0 0 1 1 3a2 2 0 0 1 2-2z"/></svg>
      (02) 4817 3960
    </li>
    <li class="contact">
      <svg viewBox="0 0 16 16" aria-hidden="true"><path d="M1 3h14v10H1z M1.8 3.6 8 8.6l6.2-5H1.8z" fill-rule="evenodd"/></svg>
      info@harborlinecrest.com
    </li>
    <li class="contact">
      <svg viewBox="0 0 16 16" aria-hidden="true"><path d="M8 1a7 7 0 1 0 0 14A7 7 0 0 0 8 1zm0 1.3c.9 0 1.9 1.7 2.2 4.2H5.8C6.1 4 7.1 2.3 8 2.3zM2.4 7.5h2.3c0 .4 0 .7.1 1H2.4a5.7 5.7 0 0 1 0-1zm3.4 1.5h4.4c-.3 2.5-1.3 4.7-2.2 4.7S6.1 11.5 5.8 9zm5.5-1.5h2.3a5.7 5.7 0 0 1 0 1h-2.4c.1-.3.1-.6.1-1z"/></svg>
      www.harborlinecrest.com
    </li>
  </ul>

  <div class="front__band"><p class="front__address">PO BOX 418 Bayview Road, 3rd street,USA</p></div>
</section>

</body>
</html>
```